Beautiful & Elegant Digital Brochure Needed For Luxury Real Estate Development

Hello,

Our company is seeking a beautiful design for our real estate development that is currently being launched.

About The Project:
Development Name - Willow Crest Estate
Location - Charleston, S.C.
Low-Country Southern Style Architecture
Google "low-country" Charleston, SC to get an idea of the unique culture of the city
Google "willow crest tree" Charleston, SC to understand the branding

Other Digital Brochures that we love

http://www.fernvalehotels.example/cedarhollow/wp-content/uploads/sites/6/2014/08/adventures-brochure.pdf

Why we like it... We love the classy feeling the brochure portrays by using unique fonts and backgrounds (burlap textures). We also love the images that represent a "low-country" vibe.

Requirements:
1. We will be providing all of the content (attached)

2. Please use plenty of southern low-country stock images from PixelVaultStock (we have a subscription so just use the watermarked images unless you have full permissions)

3. Do not copy the Cedar Hollow brochure - create a unique vision that fits in to the low-country and southern vibe

4. Attached is our logos

The font we like to use is - Caslon Antique / italic
Thank you!

Project Deadline Extended Reason: We've added more design information and we need to get more designers to participate. Added Monday, May 30, 2016

Target Market(s)

High net worth individuals - each homesite will be over 6 million dollars USD

Industry/Entity Type

Real Estate Development

Font styles to use
Script
Other font styles liked:
• Caslon Antique & Italic

Colors
abd036
00a990
acd036
9bcb3c
33b8a4
86cfc6
cfeae6

Requirements
Must have
• low country feeling
Nice to have
• burlap, wood backgrounds
Should not have
• Should NOT be corporate. This brochure is for multi-millionaire home buyers and investors. They are seeking simple, beautiful, quiet, serene, and southern lifestyles on the Intracoastal waterway on Marley Isle, Charleston, South Carolina.

```html
<!DOCTYPE html>
<html lang="en">
<head>
<meta charset="utf-8">
<title>Willow Crest Estate Brochure Spreads</title>
<link rel="stylesheet" href="https://fonts.googleapis.com/css2?family=IM+Fell+English:ital@0;1&family=Libre+Caslon+Text:ital@0;1&display=swap">
<style>
:root{
  --backdrop:#e4e3e1;
  --paper:#fbfaf6;
  --ink:#3f342a;
  --gold:#a8895a;
  --tan:#b49c78;
  --tan-soft:rgba(190,164,118,.86);
  --brown:#6a4528;
  --wood-dark:#4a2f1c;
  --wood-mid:#7a5235;
  --wood-light:#93694a;
  --cream:#f6efe2;
}
*{box-sizing:border-box;margin:0;padding:0}
html,body{width:1200px;height:1024px;overflow:hidden;background:var(--backdrop)}
body{position:relative;font-family:"Libre Caslon Text",Georgia,serif;color:var(--ink)}

.spread{position:absolute;width:560px;height:416px;background:var(--paper);overflow:hidden;box-shadow:0 2px 6px rgba(0,0,0,.12)}
.spread--legend{left:28px;top:64px}
.spread--welcome{left:612px;top:64px}
.spread--weather{left:28px;top:544px}
.spread--legends{left:612px;top:544px}
.gutter{position:absolute;top:0;bottom:0;width:24px;margin-left:-12px;background:linear-gradient(90deg,rgba(0,0,0,0),rgba(0,0,0,.10) 48%,rgba(0,0,0,.16) 50%,rgba(0,0,0,.06) 56%,rgba(0,0,0,0));pointer-events:none;z-index:5}

.block{position:absolute}
.photo{position:absolute}
.wood{position:absolute;background:
  linear-gradient(180deg,rgba(0,0,0,.10) 0 1px,transparent 1px) 0 0/100% 22px,
  linear-gradient(100deg,var(--wood-mid),var(--wood-light) 35%,var(--wood-mid) 60%,var(--wood-dark))}
.foot-bar{position:absolute;height:11px;background:var(--brown)}

.heading{font-family:"IM Fell English",Georgia,serif;font-style:italic;color:var(--gold);font-size:8.5px;line-height:11px;font-weight:400}
.heading .initial{font-size:14px;margin-right:1px}
.heading--light{color:var(--cream)}
.heading--small{font-size:6.6px;line-height:9px}
.heading--small .initial{font-size:10px}
.body{font-size:4.6px;line-height:6.8px;text-align:justify}
.body p+p{margin-top:6px}
.body--light{color:var(--cream)}
.caption{font-family:"IM Fell English",Georgia,serif;font-style:italic;font-size:5.6px;color:var(--cream)}
.quote{font-family:"IM Fell English",Georgia,serif;font-style:italic;font-size:5.4px;line-height:9px;text-align:center;color:var(--ink)}

/* spread 1 */
.legend-oak-wide{left:0;top:0;width:342px;height:196px;background:
  radial-gradient(circle at 60% 28%,#fff4c2 0,#e6cf78 5%,rgba(200,180,90,.4) 14%,transparent 26%),
  linear-gradient(180deg,#5f6e2a 0,#74802f 28%,#4d5522 48%,#3a3519 62%,#8a7a4a 80%,#b29a62)}
.legend-intro{left:23px;top:32px;width:82px;height:140px;background:var(--tan-soft);padding:6px 5px}
.legend-wood{left:342px;top:0;width:218px;height:196px}
.legend-wood-text{left:362px;top:34px;width:178px}
.legend-oak-tall{left:279px;top:190px;width:281px;height:226px;background:
  linear-gradient(180deg,#a7ba6a 0,#7c9540 22%,#55642a 45%,#4a4a26 62%,#7a6a44 80%,#a08a5e)}
.legend-caption{left:288px;top:394px}
.legend-col-a{left:19px;top:220px;width:94px}
.legend-col-b{left:134px;top:220px;width:124px}
.legend-foot{left:0;top:400px;width:60px}
.nowrap{white-space:nowrap}

/* spread 2 */
.welcome-intro{left:18px;top:22px;width:136px}
.welcome-harbor{left:166px;top:10px;width:394px;height:222px;background:
  linear-gradient(180deg,#3d8ac6 0,#7fb7dc 28%,#e8dcc0 38%,#e9c99a 44%,#c9a67a 48%,#e6b39a 56%,#b9c6c4 70%,#d8d2c4 82%,#eee6d8)}
.welcome-tree{left:166px;top:242px;width:108px;height:134px;background:
  linear-gradient(180deg,#3f5f8a 0,#8a7e9a 30%,#e0946a 48%,#f0b07a 54%,#8c8aa0 72%,#4a5270)}
.welcome-panel{left:280px;top:242px;width:280px;height:174px;background:var(--tan);padding:10px 12px}
.welcome-panel .cols{display:flex;gap:12px;margin-top:6px}
.welcome-panel .cols .body{flex:1}
.welcome-foot{left:0;top:392px;width:44px}

/* spread 3 */
.weather-grove{left:0;top:0;width:280px;height:190px;background:
  radial-gradient(circle at 64% 48%,#fbeab0 0,#eac071 14%,rgba(220,160,80,.5) 30%,transparent 50%),
  linear-gradient(180deg,#56682a 0,#7e7a34 30%,#b88a3a 60%,#9a5e22 82%,#6e3e16)}
.weather-text{left:31px;top:226px;width:222px}
.weather-foot{left:0;top:400px;width:84px}
.attractions-wood{left:310px;top:0;width:218px;height:20px}
.attractions-title{left:280px;top:42px;width:280px;text-align:center}
.attractions-quote{left:300px;top:66px;width:240px}
.marine{left:286px;top:118px;width:80px}
.paint-photo{left:374px;top:118px;width:86px;height:96px;background:linear-gradient(140deg,#ece9e2,#cfc7b8 40%,#3f78b0 58%,#2c5a8c 66%,#8b5a34)}
.pier-photo{left:286px;top:254px;width:78px;height:60px;background:linear-gradient(180deg,#2a5d93,#6ea3cc 45%,#224c7a 62%,#16355c)}
.art{left:372px;top:226px;width:90px}
.sound{left:466px;top:126px;width:84px}
.street-photo{left:466px;top:254px;width:82px;height:62px;background:linear-gradient(180deg,#5f9ad6,#b6d2ea 30%,#e6c48a 52%,#cf7f8a 72%,#6a8a4e)}
.hay{left:280px;top:326px;width:280px;height:90px;background:linear-gradient(175deg,#d8b776,#b48a48 40%,#e0c690 62%,#9a7038 85%,#c4a060)}

/* spread 4 */
.footsteps-wood{left:0;top:0;width:212px;height:196px}
.footsteps-text{left:22px;top:92px;width:170px;text-align:center}
.avenue-photo{left:212px;top:0;width:348px;height:212px;background:
  linear-gradient(180deg,#2c3a1a 0,#4e6a26 22%,#7a9a3a 42%,#a8c858 58%,#86b040 72%,#4c6e22 88%,#344c18)}
.history-a{left:14px;top:226px;width:114px}
.history-b{left:140px;top:226px;width:126px}
.isle{left:290px;top:222px;width:254px}
.legends-foot{left:0;top:396px;width:84px}
</style>
</head>
<body>

<section class="spread spread--legend" aria-label="Legend spread">
  <div class="photo legend-oak-wide" role="img" aria-label="Sunlit live oak with sprawling moss-draped limbs"></div>
  <div class="block legend-intro body body--light"><p>Nestled on pristine island land, the Willow Crest Estate community is a truly enviable home. The unspoiled maritime forest and the island's meandering coastline create a stunning natural backdrop while proximity to Charleston's world-class dining and shopping keeps culture close at hand. Wide, tree-lined streets, shaded lawns and quiet docks offer ample space to gather and to unwind. Families and friends delight in the easy, unhurried pace that defines life here. Whether you seek a peaceful retreat or a lively gathering place, the spirit of Southern hospitality welcomes every arrival.</p></div>
  <div class="wood legend-wood" role="img" aria-label="Weathered wood plank texture"></div>
  <div class="block legend-wood-text body body--light">
    <p>Island, Charleston County is home to stunning city gardens, immaculate local parks and quaint nature trails. Terrestrial wildlife is plentiful on the island and even a short hike is likely to yield amazing photo opportunities. The island is heavily populated by South Carolina's state animal, the white-tailed deer, which can be seen bounding through the wooded terrain year-round. Wild turkeys, gray foxes, squirrels, raccoons and bobcats also call the island home. For bird watchers, a close eye on the skies will yield herons, egrets, red-tailed hawks, ospreys and the occasional bald eagle soaring above the marsh. Painted buntings and warblers brighten the hedgerows each spring, while the protection of the area's natural habitat keeps the island a welcome haven for migrating birds through the changing seasons.</p>
    <p>Despite seeing an influx of visitors and new residents, a strong commitment to ecologically conscious growth promises that this natural wonderland will remain intact for generations to come. Coastal management, wildlife conservation and the protection of the area's natural resources are paramount among the considerations, and development is conducted responsibly and respectfully.</p>
  </div>
  <div class="photo legend-oak-tall" role="img" aria-label="Ancient live oak with limbs spreading across the forest floor"></div>
  <p class="block legend-caption caption">The Legend of the Willow Crest</p>
  <div class="block legend-col-a">
    <h2 class="heading nowrap"><span class="initial">T</span>he Legend of the Willow Crest</h2>
    <div class="body" style="margin-top:6px"><p>The community is named for South Carolina's enchanting Willow Crest tree, a centuries-old live oak standing at the heart of Marley Isle. Although the exact age of the tree is unknown, estimates based on its size and growth suggest that it has stood here for many hundreds of years, long before the first ships arrived along the coast. The tree's massive, sprawling branches reach outward in all directions, covering thousands of square feet of ground with deep shade. Standing tall above the lawn, its trunk measures more than twenty-five feet around, and the largest limb stretches well beyond the reach of any passing visitor. This imposing beauty has become one of the most admired natural wonders of the region, drawing admirers from near and far each year. Situated amid a treasured grove of historic oaks and quiet marsh, the tree remains a graceful reminder of Mother Nature's strength, vitality and splendor.</p></div>
  </div>
  <div class="block legend-col-b">
    <h2 class="heading" style="text-align:center"><span class="initial">E</span>mbrace Outdoor Living and Connect with Nature</h2>
    <div class="body" style="margin-top:6px">
      <p>Life is better when lived outdoors in the Lowcountry, where nature beckons. Wake each morning to breathtaking sunrises and allow the warm, salt-kissed air to rejuvenate your soul. Spend your days enjoying one of the area's exquisite beaches or visit some of Charleston's inspiring heritage sites. During the early evenings, enjoy dinner alfresco before retiring on the veranda with family and friends. Gather around an outdoor fireplace to share the day's memories and create even more under the stars.</p>
      <p>Featuring both community and private docks, Willow Crest Estate is a maritime paradise. Board your vessel to explore the tidal river separating Marley Isle from the mainland or follow the Intracoastal Waterway to the sea. For the adventurous, a kayak or canoe is an ideal means for exploring the intricacies of the island's elaborate coastal marshes. Sport fishers will be pleased to find the channels teeming with flounder, redfish, mackerel and trout, while shrimp and blue crabs abound. Non-anglers will also appreciate the plentiful array of aquatic life and availability of fresh daily seafood.</p>
    </div>
  </div>
  <div class="foot-bar legend-foot"></div>
  <div class="gutter" style="left:280px"></div>
</section>

<section class="spread spread--welcome" aria-label="Welcome spread">
  <div class="block welcome-intro">
    <h2 class="heading" style="text-align:center"><span class="initial">W</span>elcome to The Lowcountry, Where Tradition and Elegance Meet</h2>
    <div class="body" style="margin-top:12px">
      <p>Charleston has always embodied the gentility of the aristocratic South and has been a conspicuous epicenter for some of the country's finest art, architecture and cultural resources. This is flawlessly illustrated by the concentration of exquisite historic structures located throughout the city and the surrounding countryside. The city's architectural heritage has been nurtured by many groups, including Charleston's active and influential preservation society. The group, founded nearly a century ago, is the oldest of its kind anywhere in the country. Owing to their ongoing efforts, the city's historic district has seen multiple expansions as restoration projects have materialized throughout the area. The group is committed to promoting the city's historical legacy through restorative projects, preservation initiatives and education about the city's rich heritage.</p>
      <p>With new additions to the historic register as recently as the last few decades, the city's ever-growing historic district has now expanded to cover well over one hundred acres. Within these borders, nearly five thousand exquisitely preserved historic buildings stand as testament to the city's dedication to maintaining the beautiful architecture in and around the heart of the city. Picturesque examples from an array of architectural periods line city streets, beckoning tourists and inspiring awe in passers-by. Georgian, Regency and Federal, as well as Classical, Greek and Gothic Revivals are some of the most popular and most prominently featured styles, but the city is host to many homes, shops and civic buildings whose designs were inspired by other periods of architectural influence.</p>
      <p>While many buildings are being rehabilitated throughout the city, conservation efforts are also dedicated to preventing the further decline of surviving historic sites. Efforts to preserve original structures and their components have been largely successful. Throughout the city, stunning historical features in pristine condition stand as a testament to dedicated conservation efforts. Perhaps the most notable example is that some area homes still proudly feature their original crown glass windows, remarkably intact after hundreds of years. The antique glass was traditionally hand-blown by highly skilled artisans and, due to irregularities in thickness and density, it has a distinct, wavy optical quality that can be easily identified by the discerning eye.</p>
    </div>
  </div>
  <div class="photo welcome-harbor" role="img" aria-label="Historic waterfront mansions and palms beside a calm beach at dusk"></div>
  <div class="photo welcome-tree" role="img" aria-label="Bare driftwood tree reflected on the shore at sunrise"></div>
  <div class="block welcome-panel">
    <h2 class="heading heading--light"><span class="initial">N</span>ew Meets Old</h2>
    <div class="cols">
      <div class="body body--light"><p>The Lowcountry boasts a proud tradition of refined Southern grace and charming appeal. Few cities have been able to blend historic charm with modernity quite like Charleston, which has become a premier destination for those seeking to abandon the drab, predictable regularity that characterizes modern suburbs. For decades, the city has continually expanded, acquiring nearby land and welcoming new residents seeking a departure from the ordinary. While encouraging this growth, the city, local government and residents remain steadfastly dedicated to maintaining the time-honored elegance of historic Charleston.</p></div>
      <div class="body body--light"><p>The city's continued commitment to historic accuracy is widely apparent. From the period-inspired colors of the hundreds of restored homes to the careful selection of traditional materials and fixtures for renovations, no detail has been spared to maintain the area's classic beauty. By incorporating authentic, period-era building materials such as tabby, brick and locally-sourced hardwood, as well as staying true to certain architectural traditions, the city has been able to fuse modern luxury with the charming elegance of the quintessential South. Visitors will find that even the newest homes feature large, inviting porches, intricate trim and molding, and an attention to architectural detail that is often overlooked in modern construction.</p></div>
    </div>
  </div>
  <div class="foot-bar welcome-foot"></div>
  <div class="gutter" style="left:280px"></div>
</section>

<section class="spread spread--weather" aria-label="Attractions spread">
  <div class="photo weather-grove" role="img" aria-label="Golden sunlight through an old oak grove"></div>
  <div class="block weather-text">
    <h2 class="heading"><span class="initial">L</span>et the Weather Draw You Out</h2>
    <div class="body" style="margin-top:8px">
      <p>Thanks to the beautiful vistas and exceptionally good weather, the Lowcountry is a mecca for outdoor living. Because of Charleston's temperate climate, outdoor attractions are available year-round. The area boasts short, mild winters and long, hot summers. Measurable snowfall is rare, and the temperature rarely drops below freezing. Spring and fall are marked by comfortable, consistent temperatures that will coax you out of doors. Rich, well-draining soil and a consistent, temperate climate afford gardeners the luxury of a year round growing season and open the door to a wide array of landscaping options not readily enjoyed in many areas.</p>
      <p>For centuries, natives of the Lowcountry have designed their residences to take advantage of the region's enviable weather conditions and wind patterns. Large porches, sizable verandas and generous roof overhangs are conventional residential features allowing not only cover from the midday sun but also providing an ideal location to sip cocktails and entertain guests. Charlestonians relish the area's prevailing winds and their strong, cool breezes. Those breezes drift inland, sweeping through open air porches and wafting through open windows.</p>
    </div>
  </div>
  <div class="foot-bar weather-foot"></div>
  <div class="wood attractions-wood" role="img" aria-label="Weathered wood plank strip"></div>
  <h2 class="block attractions-title heading"><span class="initial">C</span>harleston's Attractions</h2>
  <p class="block attractions-quote quote">&ldquo; Whatever your interests, the Lowcountry paradise has something for everyone. Charleston offers a multitude of unique attractions that simply must be seen. &rdquo;</p>
  <div class="block marine">
    <h3 class="heading heading--small"><span class="initial">L</span>earn About Marine Life</h3>
    <div class="body" style="margin-top:3px"><p>The city's expansive aquarium offers visitors a chance to enjoy the beauty of marine life first-hand. Featuring more than five thousand indigenous and exotic species of fish, reptiles and amphibians, the aquarium invites the curious and adventurous alike. Interactive exhibits encourage visitors to get up close and personal with wildlife that is rarely seen and often misunderstood. Sea turtles, seahorses, rays and shorebirds are all waiting, while touch tanks allow guests to reach out and feel creatures of the shallows. Enthusiastic and knowledgeable volunteers are always nearby to answer questions and provide information.</p></div>
  </div>
  <div class="photo paint-photo" role="img" aria-label="Paintbrush dipped in blue paint"></div>
  <div class="photo pier-photo" role="img" aria-label="Fishing pier stretching over the ocean at twilight"></div>
  <div class="block art">
    <h3 class="heading heading--small"><span class="initial">A</span>rt in the City</h3>
    <div class="body" style="margin-top:3px"><p>In recent decades, a powerful cultural initiative has taken root in the city. Folk art and artisan crafts remain integral elements of the Charleston art scene. Arts festivals and events occur year-round and the multitude of galleries featuring original works from local and world-renowned artists is ever-expanding. Fine art galleries as well as those housing contemporary or modern works are scattered throughout the city.</p></div>
  </div>
  <div class="block sound">
    <h3 class="heading heading--small"><span class="initial">T</span>he Sound of the City</h3>
    <div class="body" style="margin-top:3px"><p>Charleston's music scene is as diverse as any other aspect of the city and the venues are nearly as important as the music itself. Visit a historic downtown church for performances inspired by its musical heritage. The weekly set includes gospel, jazz, spirituals and Civil War era hymns. Sit back and allow the music to come to you. Chamber music in the city is performed by Lowcountry musicians with a passion for classical music and historic tradition. The city's symphony orchestra performs from September through May, offering three series ranging from classical masterpieces to light-hearted pops.</p></div>
  </div>
  <div class="photo street-photo" role="img" aria-label="Colorful historic storefronts beneath a church steeple"></div>
  <div class="photo hay" role="img" aria-label="Close texture of golden straw"></div>
  <div class="gutter" style="left:280px"></div>
</section>

<section class="spread spread--legends" aria-label="History spread">
  <div class="wood footsteps-wood" role="img" aria-label="Weathered wood plank texture"></div>
  <div class="block footsteps-text">
    <h2 class="heading heading--light"><span class="initial">W</span>alk in the Footsteps of Legends</h2>
    <div class="body body--light" style="margin-top:6px;text-align:center"><p>Take a leisurely tour of Charleston's iconic row of pastel homes, once a beacon to weary sailors; paddle along one of the area's many waterways and explore the recesses of the ancient coastline; or stroll down the city's famed Battery to view the location where the first shot of the Civil War was fired. The area's rich history begs to be uncovered.</p></div>
  </div>
  <div class="photo avenue-photo" role="img" aria-label="Avenue of moss-draped live oaks over a green lawn"></div>
  <div class="block history-a body"><p>Charleston's significance to the nation's history is nearly unrivaled. One of the earliest and most important ports along the Atlantic, Charleston was founded in 1670 and named for the English crown. Charles Towne immediately became an economic center among the southern colonies. The city grew wealthy exporting rice and cotton produced along the coast and became a prominent force in the colonial trade market. Charleston flourished economically and culturally, benefiting from routinely imported luxuries such as exotic fruits, rare spices and fine silks. Charleston's prosperous landowners and elite aristocracy spared no expense on private and civic buildings and soon, the city grew to become the largest and most affluent south of Philadelphia. The city was home to the nation's first theater, and talented artists and artisans flocked to the city where their talents were highly sought and handsomely rewarded.</p></div>
  <div class="block history-b body"><p>Owing to its relatively flat terrain and readily fortified harbor islands, the city quickly became a formidable military strong point along the coast. Large sea forts were erected using logs hewn from the indigenous palmetto trees, imported granite, brick and tabby concrete. In the 1700s, Charleston's strategic position along the eastern seaboard was essential to American forces defending the harbor and the mainland from British invasion. A century later, when social tensions threatened to divide the country, Charleston again became an epicenter for social and political action. The city was host to the inaugural shot of the Civil War, not only marking the beginning of the day-long battle at the harbor fort but also signifying the official beginning of the nation's bloodiest conflict. Today, the city is the proud home of a renowned military college, one of the nation's oldest. Its impressive list of alumni includes accomplished military personnel as well as novelists, politicians, astronauts, professional athletes, actors and musicians. The college welcomes the public to many of its parades, ceremonies and events throughout the year.</p></div>
  <div class="block isle">
    <h2 class="heading"><span class="initial">A</span>bout Marley Isle</h2>
    <div class="body" style="margin-top:6px">
      <p>Set amid a network of barrier islands on the southern border of Charleston County, South Carolina, Marley Isle is a fifty square mile expanse of majestic coastal beauty. Originally occupied by native tribes, the island was first settled by Europeans in the late 17th century and, as early as the 1690s, large farming plantations were scattered along the river. Colonists also established a lucrative fur trade with the island's native tribes, shipping a surplus of deer hides to Europe during the early years. Although relations were initially amicable, a dispute over livestock brought the alliance to an end. The native legacy remains visible today, as the island's bordering rivers still bear the names of its first inhabitants.</p>
      <p>By the 1800s, the island was home to dozens of exquisite plantation homes and was known for producing a variety of crops including tea, rice, indigo and tomatoes. Many of those homes remain today as beautifully preserved testaments to the island's early agricultural heritage.</p>
      <p>In 1739, Marley Isle was home to a rebellion which claimed nearly one hundred lives. The uprising began when a band of twenty enslaved Africans took food, weapons and ammunition from a local shop before marching southward towards the Spanish territory of Florida. The group gathered followers along the route, eventually swelling to more than eighty before being intercepted by local militia forces. It was one of the largest revolts to have occurred throughout the colonies. Following the insurrection, legislation was passed prohibiting enslaved people from gathering in large groups, barring them from education and preventing owners from granting freedom. News of the rebellion traveled far and inspired a number of similar uprisings.</p>
    </div>
  </div>
  <div class="foot-bar legends-foot"></div>
  <div class="gutter" style="left:280px"></div>
</section>

</body>
</html>
```